Fitness Company Valentine's Day Special Flyer

We need an 8x10 flyer designed for our Valentine's Day Special Promo offer to the public. We've included the flyer's text and details - please include all information in the word document attached. DO NOT use this as a design template just the information. We expect something awesome!!!
- The flyer MUST be 8x10 in PSD format (CS3 Compatible) INCLUDING ALL Layers and Fonts
- Please include fitness pictures
- Include our Logo (attached)
- ***Please use the color schemes used in our logo to help with the design!!!!
Industry/Entity Type
Fitness
Look and feel
Each slider illustrates characteristics of the customer's brand and the style your logo design should communicate.

```html
<!DOCTYPE html>
<html lang="en">
<head>
<meta charset="utf-8">
<title>Pulsefit Bootcamps – Valentine's Day 2-for-1 Special</title>
<link href="https://fonts.googleapis.com/css2?family=Roboto+Condensed:wght@400;700&family=Roboto:wght@300;400;700&display=swap" rel="stylesheet">
<style>
  :root{
    --stage:#2e2420;
    --red:#ee1c25;
    --red-deep:#c4151e;
    --red-dark:#7d0d14;
    --panel-dark:#2a0b0e;
    --yellow:#ffea00;
    --white:#ffffff;
    --photo-a:#b98a6a;
    --photo-b:#4d3a33;
  }
  *{margin:0;padding:0;box-sizing:border-box}
  html,body{width:1200px;height:1200px;overflow:hidden;background:var(--stage)}
  .flyer{
    position:absolute;left:140px;top:28px;width:1008px;height:1252px;
    transform:scale(.9127);transform-origin:0 0;overflow:hidden;
    background:
      radial-gradient(circle at 70% 25%, #f0333a 0%, #d81d26 35%, #a8121b 70%, var(--red-dark) 100%);
    font-family:"Roboto Condensed",sans-serif;color:var(--white);
  }
  .abs{position:absolute}
  .shapes{position:absolute;left:0;top:0}
  .brand{left:63px;top:70px;font-weight:700;font-size:58px;line-height:60px;letter-spacing:2px}
  .headline{left:523px;top:58px;font-weight:700;line-height:1}
  .headline .day{font-size:68px}
  .headline .deal{font-size:98px;color:var(--yellow);margin-top:6px}
  .headline .special{font-size:64px;color:var(--yellow);margin-top:4px}
  .couples{left:60px;top:226px;line-height:1}
  .couples .big{font-size:72px}
  .couples .line{font-size:52px;line-height:54px}
  .benefits{left:62px;top:437px;list-style:none}
  .benefits li{display:flex;align-items:center;gap:12px;height:50px;font-weight:700;font-size:36px;color:var(--yellow)}
  .benefits svg{width:28px;height:28px;fill:var(--white)}
  .bubble-text{left:62px;top:655px;font-weight:700;line-height:1}
  .bubble-text .deal{font-size:66px}
  .bubble-text .sub{font-size:39px;line-height:48px}
  .price{left:368px;top:690px;font-family:"Roboto",sans-serif;font-weight:700;color:var(--yellow);text-shadow:3px 4px 0 #6d0a0f;white-space:nowrap}
  .price .cur{font-size:52px;vertical-align:14px}
  .price .amt{font-size:124px;letter-spacing:-2px}
  .panel-left{left:0;top:820px;width:505px;height:345px;background:linear-gradient(160deg,#3a0d11,var(--panel-dark) 60%,#4a0c12)}
  .panel-right{left:505px;top:820px;width:503px;height:345px;background:linear-gradient(180deg,#c01820,#8e1018)}
  .gift{left:62px;top:832px;font-family:"Roboto",sans-serif;font-weight:300;font-size:30px;line-height:36px}
  .jump{left:60px;top:905px;font-family:"Roboto",sans-serif;font-weight:700;white-space:nowrap}
  .jump .num{font-size:88px}
  .jump .word{font-size:44px}
  .included{left:62px;top:1005px;list-style:none;font-size:23px;line-height:28px}
  .included li{display:flex;gap:10px;margin-bottom:4px}
  .included svg{width:22px;height:22px;fill:var(--red);flex:none;margin-top:3px}
  .love{left:505px;top:826px;width:470px;text-align:center;font-weight:700;line-height:1.05}
  .love .a{font-size:46px}
  .love .b{font-size:40px}
  .offer-pill{left:523px;top:945px;width:427px;height:110px;border-radius:28px;background:var(--red)}
  .reserve{left:545px;top:948px;width:200px;text-align:center;line-height:1}
  .reserve .s{font-size:29px}
  .reserve .b{font-size:38px;font-weight:700;margin:4px 0}
  .date{left:755px;top:952px;width:180px;text-align:center;font-weight:700;line-height:1}
  .date .m{font-size:31px}
  .date .d{font-size:54px;margin-top:4px}
  .spots{left:505px;top:1076px;width:503px;text-align:center;font-size:31px}
  .call-bar{left:508px;top:1118px;width:500px;height:47px;background:rgba(255,255,255,.12);display:flex;align-items:center;gap:16px;padding-left:18px}
  .call-bar svg{width:34px;height:34px}
  .call-bar span{font-family:"Roboto",sans-serif;font-weight:700;font-size:32px;color:var(--yellow)}
  .footer{left:0;top:1165px;width:1008px;height:87px;background:var(--red-deep)}
  .footer p{font-family:"Roboto",sans-serif;font-weight:700;font-size:21px;text-align:center;padding-top:7px;padding-right:10px}
</style>
</head>
<body>
<main class="flyer">
  <svg class="shapes" width="1008" height="1252" viewBox="0 0 1008 1252">
    <defs>
      <linearGradient id="photoTone" x1="0" y1="0" x2="1" y2="1">
        <stop offset="0" stop-color="var(--photo-a)"/>
        <stop offset="1" stop-color="var(--photo-b)"/>
      </linearGradient>
    </defs>
    <path class="photo" role="img" aria-label="Photo of a smiling fitness couple in workout gear holding a water bottle outdoors"
      d="M440 650 C420 470 650 330 745 410 C780 320 900 260 1008 285 L1008 820 L440 820 Z"
      fill="url(#photoTone)" stroke="#fff" stroke-width="8"/>
    <path class="price-bubble" d="M0 820 L0 720 C40 620 250 560 330 700 C400 640 560 620 625 820 Z"
      fill="var(--red)" stroke="#fff" stroke-width="8"/>
  </svg>

  <div class="abs brand">PULSEFIT<br>BOOTCAMPS</div>

  <div class="abs headline">
    <div class="day">Valentine's Day</div>
    <div class="deal">2-FOR-1</div>
    <div class="special">SPECIAL</div>
  </div>

  <div class="abs couples">
    <div class="big">COUPLES</div>
    <div class="line">That Train Together</div>
    <div class="line">Stay Together.</div>
  </div>

  <ul class="abs benefits">
    <li><svg viewBox="0 0 24 24"><path d="M12 21s-9-5.6-9-11.5A5 5 0 0 1 12 6.5a5 5 0 0 1 9 3C21 15.4 12 21 12 21z"/></svg>MOVE BETTER</li>
    <li><svg viewBox="0 0 24 24"><path d="M12 21s-9-5.6-9-11.5A5 5 0 0 1 12 6.5a5 5 0 0 1 9 3C21 15.4 12 21 12 21z"/></svg>LOOK BETTER</li>
    <li><svg viewBox="0 0 24 24"><path d="M12 21s-9-5.6-9-11.5A5 5 0 0 1 12 6.5a5 5 0 0 1 9 3C21 15.4 12 21 12 21z"/></svg>FEEL BETTER</li>
  </ul>

  <div class="abs bubble-text">
    <div class="deal">2-FOR-1</div>
    <div class="sub">Valentine's Day</div>
    <div class="sub">Special Only</div>
  </div>
  <div class="abs price"><span class="cur">$</span><span class="amt">99</span></div>

  <section class="abs panel-left"></section>
  <section class="abs panel-right"></section>

  <p class="abs gift">The perfect gift for You and<br>Your Valentine. Included In Your</p>
  <div class="abs jump"><span class="num">30</span> <span class="word">DAY Jumpstart</span></div>
  <ul class="abs included">
    <li><svg viewBox="0 0 24 24"><path d="M12 21s-9-5.6-9-11.5A5 5 0 0 1 12 6.5a5 5 0 0 1 9 3C21 15.4 12 21 12 21z"/></svg>Success Start Consultation</li>
    <li><svg viewBox="0 0 24 24"><path d="M12 21s-9-5.6-9-11.5A5 5 0 0 1 12 6.5a5 5 0 0 1 9 3C21 15.4 12 21 12 21z"/></svg>12 Group Personal Training Sessions</li>
    <li><svg viewBox="0 0 24 24"><path d="M12 21s-9-5.6-9-11.5A5 5 0 0 1 12 6.5a5 5 0 0 1 9 3C21 15.4 12 21 12 21z"/></svg>Success Manual With Bonus Nutrition Guide</li>
    <li><svg viewBox="0 0 24 24"><path d="M12 21s-9-5.6-9-11.5A5 5 0 0 1 12 6.5a5 5 0 0 1 9 3C21 15.4 12 21 12 21z"/></svg>Unlimited Coaching Support Via Private<br>Members Group</li>
  </ul>

  <div class="abs love">
    <div class="a">LOVE YOUR BODY</div>
    <div class="b">This Valentine's Day</div>
  </div>

  <div class="abs offer-pill"></div>
  <svg class="abs" style="left:732px;top:920px" width="205" height="155" viewBox="0 0 205 155">
    <path d="M102 150 C40 115 2 85 6 50 C10 18 45 2 75 14 C90 20 98 30 104 40 C112 22 130 6 158 6 C188 8 204 32 198 62 C190 98 150 125 102 150 Z"
      fill="var(--red)" stroke="#8e1018" stroke-width="3"/>
  </svg>
  <div class="abs reserve">
    <div class="s">To Reserve This</div>
    <div class="b">OFFER!</div>
    <div class="s">Expires</div>
  </div>
  <div class="abs date">
    <div class="m">FEBRUARY</div>
    <div class="d">14th</div>
  </div>

  <p class="abs spots">ONLY 20 SPOTS AVAILABLE</p>

  <div class="abs call-bar">
    <svg viewBox="0 0 24 24"><circle cx="12" cy="12" r="11" fill="var(--red)"/><path d="M9 6.5c.4 0 .8.3.9.7l.6 2c.1.4 0 .8-.3 1l-.9.7a8 8 0 0 0 3.8 3.8l.7-.9c.3-.3.7-.4 1-.3l2 .6c.4.1.7.5.7.9v1.6c0 .6-.4 1-1 1A11 11 0 0 1 5.9 7.5c0-.6.4-1 1-1z" fill="#fff"/></svg>
    <span>Call Us - 555-014-2290</span>
  </div>

  <footer class="abs footer">
    <p>Pulsefit Bootcamps | 28 W. Elm St. Unit 9 Lakeview CO 80000 | www.pulsefitcamps.com</p>
  </footer>
</main>
</body>
</html>
```